TV - business card

Tidewell Vantage is an insurance brokerage firm, inovative, proactive, vigorous, which aims to become the leader of the insurance brokers in Anfrica. We should like to get some designs which should be avoided also in Gray / Metallic for the Administration and Orange / Blue for the Managers (ike in the picture sent). The Blue / Green logo is not the correct one, but the source of the file. Please adjust the color accordingly for the business cards. 1 / Orange / Blue 2 / Gray / Metallic We want something classic but which is transmitted strenght, inovation, modernity and most of all, rapidity. We want something start-up like, very punchy and catching eye remaining profesional at the same time. Name: Delton Ashgrove Function: Managing Director Address: N ° 73/74 Cmt. Bolembe - R / C 2B Esquerda - Bairro Quimbuta - Luanda Tel: (+244) 947 385 619 Email: delton.ashgrove@tidewell-v.com Website: www.tidewell-v. com We want classic in the front and creative, colorfull at the back. The cards will be printed in relief, with very high quality of paper.
Industry/Entity Type
Insurance Broker
Colors
Designer to choose colors to be used in the design.
Look and feel

```html
<!DOCTYPE html>
<html lang="en">
<head>
<meta charset="utf-8">
<title>Tidewell Vantage – Business Card</title>
<link href="https://fonts.googleapis.com/css2?family=Mulish:wght@400;600;700&display=swap" rel="stylesheet">
<style>
  :root {
    --backdrop: #1e1e1f;
    --card: #202122;
    --card-edge: #2a2b2c;
    --silver: #cfd0d2;
    --silver-soft: #8c8d90;
    --brand-blue: #1e9fe0;
    --ink-light: #e6e6e6;
    --ink-muted: #cfcfcf;
  }
  * { margin: 0; padding: 0; box-sizing: border-box; }
  html, body { width: 1200px; height: 900px; overflow: hidden; }
  body {
    background: var(--backdrop);
    font-family: "Mulish", sans-serif;
    position: relative;
  }
  .card {
    position: absolute;
    left: 280px;
    width: 640px;
    height: 366px;
    background: var(--card);
    border: 1px solid var(--card-edge);
    box-shadow: 0 18px 40px rgba(0,0,0,.55);
    overflow: hidden;
  }
  .card--front { top: 50px; }
  .card--back  { top: 474px; }

  /* Front */
  .front-brand {
    position: absolute;
    inset: 0;
    display: flex;
    flex-direction: column;
    align-items: center;
    justify-content: center;
    gap: 18px;
  }
  .brand-dot {
    width: 96px;
    height: 96px;
    border-radius: 50%;
    background: radial-gradient(circle at 35% 30%, #e8e8ea, #7d7e81 70%, #4a4b4d);
  }
  .brand-name {
    font-weight: 700;
    font-size: 34px;
    letter-spacing: 1px;
    color: var(--silver);
  }

  /* Back */
  .back-brand {
    position: absolute;
    left: 40px;
    top: 34px;
    font-weight: 700;
    font-size: 26px;
    letter-spacing: .5px;
    color: var(--brand-blue);
  }
  .person {
    position: absolute;
    left: 40px;
    top: 104px;
  }
  .person-name {
    font-weight: 700;
    font-size: 27px;
    letter-spacing: .8px;
    color: var(--brand-blue);
    line-height: 1;
  }
  .person-role {
    font-size: 15px;
    color: var(--ink-muted);
    margin-top: 4px;
  }
  .address {
    position: absolute;
    left: 40px;
    top: 188px;
    font-size: 16px;
    line-height: 22px;
    color: var(--ink-light);
    font-style: normal;
  }
  .contacts {
    position: absolute;
    left: 40px;
    top: 286px;
    list-style: none;
    font-size: 16px;
    line-height: 26px;
    color: var(--ink-light);
  }
  .contacts li { display: flex; align-items: center; gap: 10px; }
  .contacts svg { width: 14px; height: 14px; flex: none; }
  .back-disc {
    position: absolute;
    right: 40px;
    top: 62px;
    width: 250px;
    height: 250px;
    border-radius: 50%;
    background: radial-gradient(circle at 40% 35%, #4a4b4e, #2a2b2d 70%);
  }
</style>
</head>
<body>
  <section class="card card--front" aria-label="Card front">
    <div class="front-brand">
      <span class="brand-dot" aria-hidden="true"></span>
      <span class="brand-name">TIDEWELL-VANTAGE</span>
    </div>
  </section>

  <section class="card card--back" aria-label="Card back">
    <div class="back-brand">TIDEWELL-VANTAGE</div>
    <div class="person">
      <div class="person-name">Delton Ashgrove</div>
      <div class="person-role">Managing Director</div>
    </div>
    <address class="address">
      N ° 73/74 Cmt. Bolembe<br>
      R / C 2B Esquerda<br>
      Bairro Quimbuta - Luanda
    </address>
    <ul class="contacts">
      <li>
        <svg viewBox="0 0 24 24" aria-hidden="true"><path fill="var(--brand-blue)" d="M6.6 10.8a15.1 15.1 0 0 0 6.6 6.6l2.2-2.2a1 1 0 0 1 1-.25 11.4 11.4 0 0 0 3.6.57 1 1 0 0 1 1 1V20a1 1 0 0 1-1 1A17 17 0 0 1 3 4a1 1 0 0 1 1-1h3.5a1 1 0 0 1 1 1c0 1.25.2 2.45.57 3.57a1 1 0 0 1-.25 1z"/></svg>
        +244 947 385 619
      </li>
      <li>
        <svg viewBox="0 0 24 24" aria-hidden="true"><rect x="3" y="5" width="18" height="14" rx="1.5" fill="none" stroke="var(--brand-blue)" stroke-width="2"/><path d="M3.5 6l8.5 7 8.5-7" fill="none" stroke="var(--brand-blue)" stroke-width="2"/></svg>
        delton.ashgrove@tidewell-v.com
      </li>
    </ul>
    <span class="back-disc" aria-hidden="true"></span>
  </section>
</body>
</html>
```